Redesign of Plastic Surgeon Website to fully responsive / modern feel

Hi

Our current website is out of date www.harbourlinecosmetic.org

We want a fresh / modern looking design
Needs to be fully responsive design that works extremely well on ipad and mobile device

Would like design for both full screen website and mobile

Have listed a few websites of other plastic surgeons we like
http://www.reformclinicdaily.com/
http://www.peterholtbymd.com/
http://www.corvanbeauty.com/
http://www.tidewellcontouring.com/

Menu needs to include
1. About Us
2. Procedures (see current website for example)
3. News
4. Patient Resources
5. Contact Us

We are flexible with colours / images / layout

I have uploaded a document that has some content - the face pages content is completed only

some of the procedures can have content upwards of 4000 words - total website can be large with over 40,000 words
Updates

Target Market(s)

Mainly women 20-60 85% of practice
Some men 15%

Industry/Entity Type

Plastic Surgery

Number of Pages Required

5+ page

Requirements
Must have
• We need designs for
• Homepage
• Internal pages
• 1. Landing pages for breast / body / face / non surgical main pages
• 2. Procedure pages for individual pages under each section - eg breast augmentation
• 3. About us pages - like meet the doctor, our staff, clinics
• 4. Contact page
• 5. Blog / News page
Nice to have
• See our list of websites for examples of designs we like
• Like full screen design with nice hero image
• Needs to have good to call to action messages on home page like
• Specials, procedure of the month, etc

```html
<!DOCTYPE html>
<html lang="en">
<head>
<meta charset="utf-8">
<title>Harbourline Cosmetic – Mobile Home</title>
<link href="https://fonts.googleapis.com/css2?family=Questrial&family=Roboto:wght@400;500;700&display=swap" rel="stylesheet">
<style>
:root{
  --red:#ee2a3f;
  --ink:#2a2d3e;
  --text:#333;
  --muted:#666;
  --soft:#f6f6f6;
  --line:#c9c9c9;
  --footer:#2b2b2b;
  --footer-deep:#222;
  --footer-text:#5e5e5e;
}
*{box-sizing:border-box;margin:0;padding:0}
html,body{width:1200px;height:1200px;overflow:hidden;background:#fff}
body{position:relative;font-family:"Questrial",sans-serif;color:var(--text)}
.abs{position:absolute}
.head{font-family:"Roboto",sans-serif}

/* left column */
.brand{left:116px;top:30px;display:flex;align-items:center;gap:10px}
.brand-name{font-family:"Roboto",sans-serif;font-weight:500;color:var(--ink);font-size:30px;line-height:30px;letter-spacing:2px}
.brand-mark{width:22px;height:22px;background:var(--red)}
.nav-select{left:136px;top:103px;width:240px;height:24px;background:#eef0f3;font-size:10px;padding:0 16px;display:flex;align-items:center;justify-content:space-between}
.call{left:0;width:511px;top:140px;text-align:center;font-family:"Roboto",sans-serif;font-weight:500;font-size:13px;color:#222}
.hero{left:0;top:160px;width:511px;height:384px;background:radial-gradient(ellipse at 70% 45%,#8a1237 0%,#4b0a22 35%,#170308 75%,#0d0205 100%)}
.ribbon{left:136px;top:160px;width:240px;height:32px}
.ribbon-text{left:136px;top:160px;width:240px;height:32px;line-height:32px;text-align:center;color:#fff;font-family:"Roboto",sans-serif;font-weight:500;font-size:14px}
.hero-copy{left:64px;top:318px;width:384px;text-align:center;color:#fff}
.hero-copy .l1{font-family:"Roboto",sans-serif;font-size:18px;line-height:20px}
.hero-copy .l2{font-family:"Roboto",sans-serif;font-weight:500;font-size:23px;line-height:26px;border-bottom:1px solid rgba(255,255,255,.2);padding-bottom:2px}
.hero-copy .l3{font-size:19px;line-height:26px}
.learn{left:136px;top:416px;width:240px;height:32px;background:rgba(40,40,58,.85);color:var(--red);font-family:"Roboto",sans-serif;font-weight:500;font-size:12px;display:flex;align-items:center;justify-content:center}
.welcome h2{position:absolute;left:40px;top:568px;font-family:"Roboto",sans-serif;font-weight:500;font-size:19px;color:var(--ink)}
.copy{left:40px;width:435px;font-size:11.6px;line-height:14.4px;color:#333}
.vision{left:40px;top:744px;width:432px;height:80px;border-left:3px solid #ccc;padding-left:21px}
.vision h3{font-family:"Roboto",sans-serif;font-weight:500;font-size:14px;color:var(--ink);margin:4px 0 12px}
.vision p{font-size:11.6px;line-height:14.4px}
.promo-bg{left:0;top:848px;width:511px;height:352px;background:var(--soft)}
.tile{left:40px;width:432px}
.tile-label{left:112px;width:288px;height:40px;border:1px solid var(--red);background:rgba(230,225,226,.7);color:#3a3340;font-family:"Roboto",sans-serif;font-weight:500;font-size:14.5px;display:flex;align-items:center;justify-content:center}

/* right column */
.top-bg{left:688px;top:0;width:512px;height:208px;background:var(--soft)}
.meet-img{left:728px;top:0;width:432px;height:56px;background:linear-gradient(90deg,#9a6a57,#c28c72,#b27e6b)}
.spec-img{left:728px;top:56px;width:432px;height:128px;background:linear-gradient(180deg,#a7685a 0%,#8e4d45 55%,#b26d57 100%)}
.meet{left:800px;top:0;width:288px;height:40px;background:var(--red);color:#fff;font-family:"Roboto",sans-serif;font-weight:500;font-size:14px;display:flex;align-items:center;justify-content:center}
.meet-dot{left:1036px;top:-16px;width:36px;height:36px;border-radius:50%;background:rgba(255,255,255,.35)}
.specials{left:800px;top:101px;width:288px;height:39px;border:1px solid var(--red);background:rgba(230,225,226,.7);color:#3a3340;font-family:"Roboto",sans-serif;font-weight:500;font-size:14px;display:flex;align-items:center;justify-content:center}
.contact-title{left:688px;width:512px;top:232px;text-align:center;font-family:"Roboto",sans-serif;font-weight:500;font-size:19px;color:var(--ink)}
.field{border:1px solid var(--line);font-size:11.6px;color:#333;padding:13px 14px}
.submit{left:840px;top:464px;width:208px;height:32px;background:var(--red);color:#fff;font-family:"Roboto",sans-serif;font-weight:500;font-size:14px;display:flex;align-items:center;justify-content:center}
.partners-bg{left:688px;top:528px;width:512px;height:176px;background:var(--soft)}
.partners-title{left:688px;width:512px;top:549px;text-align:center;font-family:"Roboto",sans-serif;font-weight:500;font-size:14px;color:var(--ink)}
.badge{background:#ececec;border-radius:4px}
.footer{left:688px;top:704px;width:512px;height:448px;background:var(--footer)}
.footer-bar{left:688px;top:1152px;width:512px;height:48px;background:var(--footer-deep)}
.f-title{font-family:"Roboto",sans-serif;font-weight:500;font-size:12px;color:#e8e8e8}
.f-muted{font-size:11.6px;line-height:14.4px;color:var(--footer-text)}
.f-item{display:flex;gap:14px;width:208px}
.f-item .sq{width:32px;height:32px;flex:none}
.f-item p{font-size:11.6px;line-height:14.4px;color:#ddd}
.f-item span{display:block;color:var(--footer-text);margin-top:2px;font-family:"Roboto",sans-serif;font-size:11px}
.f-sep{height:1px;background:#3a3a3a;width:208px}
.f-link{font-size:11.6px;line-height:14.4px;color:#ddd}
.social{width:24px;height:24px;background:#fff}
.legal{font-family:"Roboto",sans-serif;font-weight:500;font-size:10px;color:#ddd}
</style>
</head>
<body>

<!-- LEFT COLUMN -->
<div class="abs brand"><div class="brand-name">HARBOURLINE<br>COSMETIC</div><div class="brand-mark"></div></div>
<div class="abs nav-select"><span>Home</span>
  <svg width="12" height="8" viewBox="0 0 12 8"><path d="M1 1l5 5 5-5" stroke="#333" stroke-width="1.8" fill="none"/></svg>
</div>
<div class="abs call">CALL FOR APPOINTMENTS</div>

<div class="abs hero" role="img" aria-label="Hero photograph: woman draped in crimson silk against a dark curtain"></div>
<svg class="abs ribbon" viewBox="0 0 240 32" width="240" height="32"><path d="M0 0H240L228 16L240 32H0L12 16Z" fill="#ee2a3f"/></svg>
<div class="abs ribbon-text">02 9174 3620</div>
<div class="abs hero-copy">
  <div class="l1">AT THE INSTITUTE OF</div>
  <div class="l2">COSMETIC RENEWAL SURGERY</div>
  <div class="l3">Your future looks beautiful.</div>
</div>
<div class="abs learn">LEARN MORE</div>

<section class="welcome">
  <h2>WELCOME TO HLC</h2>
  <p class="abs copy" style="top:599px">You can expect beautiful results at the Institute of Cosmetic Renewal. Offering unparalleled expertise in face, breast and body enhancement, including facelifts, breast augmentation / lift / reduction or tummy tucks, we offer total care at every step of your transformative journey.</p>
  <p class="abs copy" style="top:671px">Dr Halloway is one of Australia's most eminent specialists in plastic and cosmetic surgery, and is supported by our highly qualified, professional team. As Sydney's premier plastic surgery clinic, we use only the most revolutionary techniques to minimise scarring to help you look better, feel better and enjoy a beautiful new you.</p>
  <div class="abs vision">
    <h3>OUR VISION</h3>
    <p>With advanced techniques, expertise and constant client feedback, we aim to remain at the forefront of surgical rejuvenation and deliver outstanding results for clients who value experience, empathy and quality outcomes.</p>
  </div>
</section>

<div class="abs promo-bg"></div>
<div class="abs tile" style="top:872px;height:128px;background:linear-gradient(135deg,#a47b72,#b8877c,#9c6f67)" role="img" aria-label="Close-up beauty photograph of a woman with colourful makeup"></div>
<div class="abs tile" style="top:1000px;height:128px;background:linear-gradient(180deg,#6e2a35,#5a1f2a)" role="img" aria-label="Photograph of two women in head wraps, mirrored"></div>
<div class="abs tile" style="top:1128px;height:72px;background:linear-gradient(90deg,#f0bfb0,#e6a890,#c98b6e)" role="img" aria-label="Soft-focus photograph of a smiling woman"></div>
<div class="abs tile-label" style="top:920px">PROCEDURE OF THE MONTH</div>
<div class="abs tile-label" style="top:1044px">FAT FREEZING / BODY CONTOURING</div>

<!-- RIGHT COLUMN -->
<div class="abs top-bg"></div>
<div class="abs meet-img" role="img" aria-label="Warm-toned photograph behind the doctor link"></div>
<div class="abs spec-img" role="img" aria-label="Photograph of a woman in a headscarf, tinted rose"></div>
<div class="abs meet">MEET DR HALLOWAY</div>
<div class="abs meet-dot"></div>
<div class="abs specials">SPECIALS</div>

<div class="abs contact-title">CONTACT US</div>
<div class="abs field" style="left:728px;top:280px;width:208px;height:40px">First Name</div>
<div class="abs field" style="left:952px;top:280px;width:208px;height:40px">Last Name</div>
<div class="abs field" style="left:728px;top:332px;width:208px;height:40px">E-mail Address</div>
<div class="abs field" style="left:952px;top:332px;width:208px;height:40px">Subject</div>
<div class="abs field" style="left:728px;top:384px;width:432px;height:64px">Your Message</div>
<div class="abs submit">SUBMIT</div>

<div class="abs partners-bg"></div>
<div class="abs partners-title">PARTNERS</div>
<div class="abs badge" style="left:764px;top:582px;width:140px;height:32px"></div>
<div class="abs badge" style="left:1000px;top:580px;width:108px;height:34px"></div>
<div class="abs badge" style="left:790px;top:636px;width:96px;height:48px"></div>
<div class="abs badge" style="left:996px;top:644px;width:128px;height:40px"></div>

<div class="abs footer"></div>
<div class="abs f-title" style="left:728px;top:732px">About Us</div>
<p class="abs f-muted" style="left:728px;top:756px;width:432px">Our nursing and patient support teams sole goal is to support our patients who trust us with their care. You can feel confident of their support and expertise at every step of your transformative journey. We treat every patient with absolute respect, so you can be comfortable in our sincere, friendly and supportive environment.</p>

<div class="abs f-title" style="left:728px;top:852px">Recent Posts</div>
<div class="abs f-title" style="left:951px;top:852px">Latest Tweets</div>
<div class="abs f-item" style="left:728px;top:878px"><div class="sq" style="background:var(--red)"></div><p>Your Treatment at Institute of Cosmetic Renewal<span>on 12 Jan, 2016</span></p></div>
<div class="abs f-sep" style="left:728px;top:931px"></div>
<div class="abs f-item" style="left:728px;top:942px"><div class="sq" style="background:var(--red)"></div><p>Your Treatment at Institute of Cosmetic Renewal<span>on 12 Jan, 2016</span></p></div>
<div class="abs f-item" style="left:952px;top:878px"><div class="sq" style="background:#555"></div><p>Your Treatment at Institute of Cosmetic Renewal<span>on 12 Jan, 2016</span></p></div>
<div class="abs f-sep" style="left:952px;top:931px"></div>
<div class="abs f-item" style="left:952px;top:942px"><div class="sq" style="background:#555"></div><p>Your Treatment at Institute of Cosmetic Renewal<span>on 12 Jan, 2016</span></p></div>

<div class="abs f-title" style="left:727px;top:1012px">Lastest Articles</div>
<p class="abs f-link" style="left:728px;top:1036px;width:210px">Forehead and eyebrow lift to address the wrinkles Plastic Surgery.</p>
<p class="abs f-link" style="left:728px;top:1076px;width:210px">Nose surgery is a procedure to reshape</p>
<div class="abs f-title" style="left:952px;top:1013px">Stay Connected</div>
<p class="abs f-muted" style="left:952px;top:1036px;width:208px">Forehead and eyebrow lift to address the wrinkles</p>
<div class="abs social" style="left:952px;top:1072px"></div>
<div class="abs social" style="left:984px;top:1072px"></div>
<div class="abs social" style="left:1016px;top:1072px"></div>

<div class="abs footer-bar"></div>
<div class="abs legal" style="left:727px;top:1171px">Copyrights © 2016 harbourlinecosmetic. All Rights Reserved</div>
<div class="abs legal" style="left:1049px;top:1171px">Site Map | Privacy Policy</div>

</body>
</html>
```